Business Card Tevan Law llc examples and ideas are attached.

in addition to the logo we need a desription what we do: "Reprsenting students with disabilites obtain services to progress in the public school system."

If you can squeeze it on the fron at the bottom great if not put it on the back

```html
<!DOCTYPE html>
<html lang="en">
<head>
<meta charset="utf-8">
<title>Tevan Law llc — Business Card</title>
<link rel="stylesheet" href="https://fonts.googleapis.com/css2?family=Alegreya:ital,wght@1,700&family=Crimson+Pro:ital,wght@0,400;1,400&display=swap">
<style>
  :root {
    --paper: #ffffff;
    --ink: #111111;
    --navy: #00305f;
    --gold: #9a7f45;
  }
  html, body {
    margin: 0;
    padding: 0;
    overflow: hidden;
    background: var(--paper);
  }
  .card {
    position: relative;
    width: 1200px;
    height: 873px;
    background: var(--paper);
    color: var(--ink);
    overflow: hidden;
  }
  .brand-mark {
    position: absolute;
    left: 80px;
    top: 220px;
    width: 399px;
    height: 399px;
    background: var(--navy);
    display: flex;
    align-items: center;
    justify-content: center;
  }
  .brand-mark__name {
    font-family: "Alegreya", Georgia, serif;
    font-style: italic;
    font-weight: 700;
    font-size: 58px;
    color: var(--gold);
    line-height: 1;
  }
  .divider {
    position: absolute;
    left: 532px;
    top: 212px;
    width: 4px;
    height: 534px;
    background: var(--ink);
  }
  .text {
    position: absolute;
    margin: 0;
    line-height: 1;
    white-space: nowrap;
  }
  .bold-italic {
    font-family: "Alegreya", Georgia, serif;
    font-style: italic;
    font-weight: 700;
  }
  .regular {
    font-family: "Crimson Pro", Georgia, serif;
    font-weight: 400;
  }
  .firm-name   { left: 587px; top: 266px; font-size: 54px; }
  .person-name { left: 647px; top: 356px; font-size: 43px; }
  .person-role { left: 647px; top: 403px; font-size: 40px; }
  .street      { left: 647px; top: 474px; font-size: 34px; }
  .city        { left: 647px; top: 524px; font-size: 40px; }
  .hours       { left: 647px; top: 567px; font-size: 37px; font-style: italic; }
  .phone       { left: 647px; top: 636px; font-size: 35px; }
  .email       { left: 654px; top: 682px; font-size: 40px; }
  .street sup  { font-size: 0.5em; vertical-align: 0.9em; }
  .tagline {
    left: 58px;
    top: 796px;
    font-size: 23px;
  }
</style>
</head>
<body>
  <main class="card">
    <div class="brand-mark">
      <span class="brand-mark__name">Tevan Law</span>
    </div>

    <div class="divider"></div>

    <h1 class="text bold-italic firm-name">Tevan Law llc</h1>
    <p class="text bold-italic person-name">Dario M Tevan</p>
    <p class="text regular person-role">Attorney at low</p>

    <p class="text bold-italic street">1458 NE 21<sup>st</sup>Ave</p>
    <p class="text regular city">Fort Lauderdale FL 33304</p>
    <p class="text regular hours">By appointment only</p>

    <p class="text bold-italic phone">+813 555 0142</p>
    <p class="text regular email">dario.tevanlow@inboxmail.com</p>

    <p class="text bold-italic tagline">Reprsenting students with disabilites obtain services to progress in the public school system.</p>
  </main>
</body>
</html>
```